Business card design for IT consulting company

Looking for a simple, modern, clean business card design.
Open to reworking our existing logo.

Attached is our current business cards which we do not like.
Ideally double sided with something simple on the back.
Rectangle / Horizonal only.
No rounded edges on the card.
White as the dominate color is preferred.

Target Market(s)

clients, legal, oil & gas, medical, professionals

Industry/Entity Type

IT, tech, consulting

Contact Information for Business Card

Name, Title, email, phone, cell, website

Font styles to use
Sans Serif

Requirements
Must have
• Clean design
Should not have
• loud colors or unusual fonts, etc

```html
<!DOCTYPE html>
<html lang="en">
<head>
<meta charset="utf-8">
<title>Orvel Solutions – Business Card</title>
<link href="https://fonts.googleapis.com/css2?family=Inter:wght@700&family=Source+Sans+3:wght@400;600&display=swap" rel="stylesheet">
<style>
  :root {
    --bg: #e4e4e4;
    --paper: #f7f7f8;
    --ink-dark: #1b1b1c;
    --ink-logo: #161616;
    --white: #ffffff;
    --yellow: #f4bd2f;
    --red: #e5404f;
    --navy: #26256b;
    --blue: #37a6dd;
    --contact: #f0f0f0;
  }
  html, body {
    margin: 0;
    width: 1200px;
    height: 1200px;
    overflow: hidden;
    background: var(--bg);
    font-family: "Source Sans 3", "Helvetica Neue", Arial, sans-serif;
  }
  .card {
    position: absolute;
    left: 262px;
    width: 686px;
    height: 392px;
    box-sizing: border-box;
  }

  /* Front */
  .card-front { top: 165px; background: var(--paper); }
  .front-identity { position: absolute; left: 47px; top: 96px; }
  .person-name {
    margin: 0;
    font-weight: 600;
    font-size: 27px;
    line-height: 1;
    color: var(--yellow);
  }
  .person-title {
    margin: 5px 0 0;
    font-weight: 400;
    font-size: 16px;
    color: var(--blue);
  }
  .brand {
    display: flex;
    align-items: center;
    font-family: "Inter", "Helvetica Neue", Arial, sans-serif;
    font-weight: 700;
    letter-spacing: -0.5px;
  }
  .brand-square { flex: none; border-radius: 5px; }
  .front-brand {
    position: absolute;
    right: 47px;
    top: 81px;
    font-size: 38px;
    color: var(--ink-logo);
  }
  .front-brand .brand-square { width: 76px; height: 76px; margin-right: 14px; background: var(--yellow); }

  .colour-rule {
    position: absolute;
    left: 0; right: 0; top: 243px;
    display: flex;
    gap: 5px;
    height: 3px;
  }
  .colour-rule span { flex: 1; }
  .colour-rule .yellow { background: var(--yellow); }
  .colour-rule .red { background: var(--red); }
  .colour-rule .navy { background: var(--navy); }
  .colour-rule .blue { background: var(--blue); }

  .contact-band {
    position: absolute;
    left: 0; right: 0; bottom: 0;
    height: 141px;
    background: var(--ink-dark);
    color: var(--contact);
    font-size: 20px;
  }
  .contact-list {
    position: absolute;
    top: 44px;
    margin: 0; padding: 0;
    list-style: none;
  }
  .contact-list li { display: flex; align-items: center; height: 26px; }
  .contact-list svg { width: 15px; height: 15px; fill: var(--red); flex: none; }
  .contact-phones { left: 47px; }
  .contact-phones svg { margin-right: 8px; }
  .contact-online { right: 47px; }
  .contact-online li { justify-content: flex-end; }
  .contact-online svg { margin-left: 12px; }

  /* Back */
  .card-back {
    top: 653px;
    background: linear-gradient(180deg, #222223 0%, #1b1b1c 100%);
  }
  .back-brand {
    position: absolute;
    left: 0; right: 0; top: 138px;
    justify-content: center;
    font-size: 58px;
    color: var(--white);
  }
  .back-brand .brand-square { width: 115px; height: 115px; margin-right: 20px; background: var(--yellow); }
  .back-web {
    position: absolute;
    left: 0; right: 0; top: 313px;
    text-align: center;
    font-family: "Inter", "Helvetica Neue", Arial, sans-serif;
    font-weight: 700;
    font-size: 16px;
    letter-spacing: 4.5px;
    color: var(--white);
  }
</style>
</head>
<body>

<section class="card card-front" aria-label="Card front">
  <div class="front-identity">
    <p class="person-name">Daniel Reyes</p>
    <p class="person-title">IT Consultant</p>
  </div>

  <div class="brand front-brand">
    <span class="brand-square"></span>
    <span class="brand-name">Orvel Solutions</span>
  </div>

  <div class="colour-rule">
    <span class="yellow"></span><span class="red"></span><span class="navy"></span><span class="blue"></span>
  </div>

  <div class="contact-band">
    <ul class="contact-list contact-phones">
      <li>
        <svg viewBox="0 0 24 24" aria-hidden="true"><path d="M6.6 10.8a15.1 15.1 0 0 0 6.6 6.6l2.2-2.2a1 1 0 0 1 1-.25 11.4 11.4 0 0 0 3.6.57 1 1 0 0 1 1 1V20a1 1 0 0 1-1 1A17 17 0 0 1 3 4a1 1 0 0 1 1-1h3.5a1 1 0 0 1 1 1c0 1.25.2 2.45.57 3.57a1 1 0 0 1-.25 1z"/></svg>
        (888) 555-0142
      </li>
      <li>
        <svg viewBox="0 0 24 24" aria-hidden="true"><path d="M7 1h10a2 2 0 0 1 2 2v18a2 2 0 0 1-2 2H7a2 2 0 0 1-2-2V3a2 2 0 0 1 2-2zm0 3v15h10V4z"/></svg>
        (604) 555-0187
      </li>
    </ul>
    <ul class="contact-list contact-online">
      <li>
        daniel.reyes@orvel.ca
        <svg viewBox="0 0 24 24" aria-hidden="true"><path d="M2 6h20v2l-10 6L2 8zm0 4.3 10 6 10-6V19H2z"/></svg>
      </li>
      <li>
        www.orvel.ca
        <svg viewBox="0 0 24 24" aria-hidden="true"><path d="M12 2a10 10 0 1 0 0 20 10 10 0 0 0 0-20zm-1 17.9A8 8 0 0 1 4.2 10L9 14.8v1a2 2 0 0 0 2 2zm6.9-2.5A2 2 0 0 0 16 16h-1v-3a1 1 0 0 0-1-1H8v-2h2a1 1 0 0 0 1-1V7h2a2 2 0 0 0 2-2v-.4a8 8 0 0 1 2.9 12.8z"/></svg>
      </li>
    </ul>
  </div>
</section>

<section class="card card-back" aria-label="Card back">
  <div class="brand back-brand">
    <span class="brand-square"></span>
    <span class="brand-name">Orvel Solutions</span>
  </div>
  <div class="back-web">www.orvel.com</div>
</section>

</body>
</html>
```